Soho based IT support firm flyer.

We need a flyer to boost our business. We're a tech support firm based in Soho, London and provide helpdesk and call out support to SMEs in and around London.
They'll be two flyers with the same design. One is location specific and has the copy:
-
1 Month Free IT Support!
Based in Soho, we provide expert tech support for both Zelks and PCs.
We have monthly as well as pay-as-you-go plans to fit your business.
Call us now and we'll show you how we can save you up to 50% on your IT spend.
-None location based is-
1 Month Free IT Support!
We provide expert, professional tech support for both Zelks and PCs.
• Dedicated full time helpdesk
• Same day onsite visits
• Proactive support with monitoring
• 98% satisfaction score*
*taken from satisfaction survey sent out on closure of every case for Oct 2011 to Oct 2012
-
The location one needs to include a map with our location marked as postcode Q9X 4TT.
I'm fine with royalty photos being used within a reasonable price. Please use PicturVault.
Our site shows our brand best. Please keep as close to this as possible.
http://brivo-desk.example
Thanks for looking.

```html
<!DOCTYPE html>
<html lang="en">
<head>
<meta charset="utf-8">
<title>Brivo Desk – IT Support Flyer</title>
<link rel="stylesheet" href="https://fonts.googleapis.com/css2?family=Roboto+Slab:wght@300;400&display=swap">
<style>
  :root {
    --forest: #0f4a23;
    --leaf: #4a8530;
    --lime: #c5d92f;
    --ink: #ffffff;
    --soft-ink: #dfe9d6;
    --page: #ffffff;
    --rule: #8fa53a;
  }
  * { margin: 0; padding: 0; box-sizing: border-box; }
  html, body { width: 1200px; height: 900px; overflow: hidden; background: var(--page); }
  body { position: relative; font-family: "Roboto Slab", Georgia, serif; font-weight: 300; color: var(--ink); }

  .flyer { position: absolute; left: 302px; top: 29px; width: 595px; height: 841px; background: var(--page); }

  .hero { position: absolute; left: 0; top: 0; width: 595px; height: 441px; background: var(--forest); }
  .hero__title { position: absolute; top: 54px; width: 100%; text-align: center; font-size: 58px; font-weight: 300; letter-spacing: 0.5px; }
  .hero__title .accent { color: var(--lime); }

  .offer { position: absolute; right: 373px; top: 170px; text-align: right; font-size: 38px; line-height: 40px; font-weight: 300; }
  .divider-v { position: absolute; left: 239px; top: 166px; width: 1px; height: 126px; background: var(--rule); }
  .divider-h { position: absolute; left: 239px; top: 249px; width: 316px; height: 1px; background: var(--rule); }
  .divider-tick { position: absolute; left: 555px; top: 231px; width: 1px; height: 38px; background: var(--rule); }

  .pitch { position: absolute; left: 270px; font-size: 13.5px; line-height: 18.5px; color: var(--soft-ink); width: 290px; }
  .pitch--intro { top: 169px; }
  .pitch--call { top: 257px; }

  .footnote { position: absolute; left: 355px; top: 363px; width: 195px; text-align: center; font-size: 11.5px; line-height: 14.5px; text-transform: uppercase; color: var(--soft-ink); }

  .photo { position: absolute; left: 0; top: 444px; width: 595px; height: 264px;
    background: linear-gradient(90deg, #5f8a2e 0%, #8fb04a 10%, #c7d88a 45%, #a9c45a 70%, #6f9636 100%); }

  .feature-panel { position: absolute; left: 42px; top: 343px; width: 246px; height: 390px; }
  .feature-panel svg { position: absolute; left: 0; top: 0; }
  .feature-panel__reflection { position: absolute; left: 42px; top: 733px; width: 246px; height: 36px;
    background: linear-gradient(#cfcfcf, rgba(255,255,255,0)); }
  .feature-panel__heading { position: absolute; top: 45px; width: 100%; text-align: center; color: var(--lime); font-size: 27px; line-height: 27px; font-weight: 300; }
  .feature-list { position: absolute; top: 168px; width: 100%; list-style: none; text-align: center; }
  .feature-list li.small { font-size: 14.5px; line-height: 20px; }
  .feature-list li.large { font-size: 20px; line-height: 25px; }
  .feature-list li.score { font-size: 14.5px; line-height: 24px; color: var(--soft-ink); }
  .feature-panel__dots { position: absolute; left: 34px; top: 272px; width: 178px; border-top: 1px dotted #a7c27a; }
  .map { position: absolute; left: 56px; top: 287px; width: 137px; height: 112px;
    background: linear-gradient(160deg, #ece9e1, #e3dfd3 60%, #d9d6c6); }

  .brand { position: absolute; left: 344px; top: 730px; font-size: 38px; font-weight: 400; color: var(--leaf); }

  .contact-bar { position: absolute; left: 0; top: 797px; width: 595px; height: 44px; background: var(--forest);
    font-size: 12.5px; line-height: 44px; text-align: center; color: var(--soft-ink); }
</style>
</head>
<body>
<main class="flyer">
  <section class="hero">
    <h1 class="hero__title"><span class="accent">BRIVO</span> DESK</h1>
    <p class="offer">1 Month<br>Free IT<br>Support!</p>
    <span class="divider-v"></span>
    <span class="divider-h"></span>
    <span class="divider-tick"></span>
    <p class="pitch pitch--intro">Based in Soho, we provide expert tech support for both Zelks and PCs.<br>We have monthly as well as pay-as-you-go plans to fit your business.</p>
    <p class="pitch pitch--call">Call us now and we’ll show you how we can save you up to 50% on your IT spend.</p>
    <p class="footnote">*Taken from satisfaction survey sent out on closure of every case for Oct 2011 to Oct 2012</p>
  </section>

  <div class="photo" role="img" aria-label="Photo of two business people smiling at a laptop against a soft green leafy background"></div>

  <div class="feature-panel__reflection"></div>
  <aside class="feature-panel">
    <svg width="246" height="390" viewBox="0 0 246 390" aria-hidden="true">
      <polygon points="0,30 123,0 246,30 246,390 0,390" fill="var(--leaf)"/>
    </svg>
    <h2 class="feature-panel__heading">DEDICATE<br>FULL TIME<br>HELPDESK</h2>
    <ul class="feature-list">
      <li class="small">Same day onsite visits</li>
      <li class="large">Proactive support</li>
      <li class="large">with monitoring</li>
      <li class="score">98% satisfaction score*</li>
    </ul>
    <span class="feature-panel__dots"></span>
    <div class="map" role="img" aria-label="Street map of Soho with the office location marked at postcode Q9X 4TT"></div>
  </aside>

  <p class="brand">Brivo Desk</p>

  <footer class="contact-bar">12-14 Marlow House, Larch Street, London Q9X 4TT – 0200 000 4812 – info@brivo-desk.example</footer>
</main>
</body>
</html>
```